New Managed IT company needs a business card

We are an IT management and support company that needs a business card design. I have a logo that I'll provide. Blues and blacks match the logo, but i'm open to anything. I want the card to help people take us seriously, but still have some energy and fun in it. The card should communicate stability and a solid company.

Target Market(s)

Target market includes Owners and Presidents at small businesses of 20 - 100 employees in the Pittsburgh PA area.

Industry/Entity Type

Information Technology

Contact Information for Business Card

i am open to other designs, but i imagine having only the logo on one side and then the logo plus all contact details on the other side.

Requirements
Must have
• Our logo
• Company name is optional if the logo makes it obvious
• A name - Cole Perrin
• A title - President
• A phone number - 724-XXX-XXXX
• A mobile phone number - 724-615-2748
• An email address - cperrin@techvaultgrid.com
• a website - techvaultgrid.com or www.techvaultgrid.com
Nice to have
• some people tell me the logo feels like a superhero theme, some fun with that idea might be good. I'm open to ideas.
Should not have
• stock photos of people or computers - especially old looking stuff.

```html
<!DOCTYPE html>
<html lang="en">
<head>
<meta charset="utf-8">
<title>TechVault Grid – Business Card</title>
<link rel="stylesheet" href="https://fonts.googleapis.com/css2?family=Montserrat:wght@700&family=Questrial&display=swap">
<style>
  :root{
    --page:#fdfdfd;
    --card:#c5c4c5;
    --ink:#111111;
    --icon-hex:#56595b;
    --icon-glyph:#2a9ad8;
    --blue-deep:#0e56a8;
    --blue:#1e86c8;
    --blue-light:#6ccdf2;
    --charcoal:#2d2e2e;
    --black:#0c0d0f;
  }
  *{margin:0;padding:0;box-sizing:border-box}
  html,body{width:1200px;height:1200px;overflow:hidden;background:var(--page)}
  .canvas{position:relative;width:1200px;height:1200px;background:var(--page)}
  .card{position:absolute;left:0;top:284px;width:1200px;height:632px;background:var(--card);overflow:hidden}
  .card__art{position:absolute;right:0;top:0;width:720px;height:632px}
  .holder{position:absolute;left:36px;top:100px;color:var(--ink)}
  .holder__name{font-family:"Montserrat",sans-serif;font-weight:700;font-size:48px;line-height:1;letter-spacing:.2px}
  .holder__title{font-family:"Questrial",sans-serif;font-size:35px;line-height:1;margin-top:8px}
  .contact{position:absolute;left:0;font-family:"Questrial",sans-serif;font-size:30px;color:var(--ink);line-height:38px}
  .contact__icon{position:absolute;left:50px;width:36px;height:38px}
  .contact__text{position:absolute;white-space:nowrap}
  .contact--phone .contact__icon{top:223px}
  .contact--phone .contact__text{left:114px;top:211px}
  .contact--email .contact__icon{top:308px}
  .contact--email .contact__text{left:114px;top:305px}
  .contact--web .contact__icon{top:375px}
  .contact--web .contact__text{left:120px;top:372px}
  .brand{position:absolute;left:34px;top:484px;width:200px;text-align:center}
  .brand__dot{display:block;width:66px;height:66px;border-radius:50%;background:var(--blue);margin:0 auto 10px}
  .brand__name{font-family:"Questrial",sans-serif;font-size:26px;color:var(--ink);letter-spacing:1px;white-space:nowrap}
</style>
</head>
<body>
<div class="canvas">
  <section class="card">
    <svg class="card__art" viewBox="0 0 720 632" role="img" aria-label="Abstract faceted geometric artwork in blues, greys and black, shards scattering leftward">
      <defs>
        <linearGradient id="facetTone" x1="0" y1="0" x2="1" y2="0">
          <stop offset="0" stop-color="#c5c4c5" stop-opacity="0"/>
          <stop offset="0.25" stop-color="#8fa3b5"/>
          <stop offset="0.55" stop-color="#1e86c8"/>
          <stop offset="0.8" stop-color="#0e56a8"/>
          <stop offset="1" stop-color="#2d2e2e"/>
        </linearGradient>
      </defs>
      <rect x="0" y="0" width="720" height="632" fill="url(#facetTone)"/>
    </svg>

    <div class="holder">
      <h1 class="holder__name">Cole Perrin</h1>
      <p class="holder__title">President</p>
    </div>

    <div class="contact contact--phone">
      <svg class="contact__icon" viewBox="0 0 36 38" aria-hidden="true">
        <polygon points="18,1 34,10 34,28 18,37 2,28 2,10" fill="var(--icon-hex)"/>
        <path d="M12 11c1-1 2-1 3 0l1.5 2.5c.4.8.2 1.5-.5 2l-1 .8c.8 2 2.2 3.5 4 4.4l.9-1c.6-.6 1.3-.7 2-.3l2.4 1.6c.9.7.9 1.7 0 2.7-1.3 1.4-3 1.8-4.8.8-3.6-1.9-6.4-4.8-8.2-8.6-.8-1.8-.6-3.4.7-4.9z" fill="var(--icon-glyph)"/>
      </svg>
      <p class="contact__text">724-XXX-XXXX<br>724-615-2748</p>
    </div>

    <div class="contact contact--email">
      <svg class="contact__icon" viewBox="0 0 36 38" aria-hidden="true">
        <polygon points="18,1 34,10 34,28 18,37 2,28 2,10" fill="var(--icon-hex)"/>
        <rect x="9" y="13" width="18" height="12" fill="var(--icon-glyph)"/>
        <polyline points="9,13 18,20 27,13" fill="none" stroke="#dff2fb" stroke-width="1.4"/>
      </svg>
      <p class="contact__text">cperrin@techvaultgrid.com</p>
    </div>

    <div class="contact contact--web">
      <svg class="contact__icon" viewBox="0 0 36 38" aria-hidden="true">
        <polygon points="18,1 34,10 34,28 18,37 2,28 2,10" fill="var(--icon-hex)"/>
        <g fill="none" stroke="var(--icon-glyph)" stroke-width="1.5">
          <circle cx="18" cy="19" r="8.5"/>
          <ellipse cx="18" cy="19" rx="3.8" ry="8.5"/>
          <line x1="9.5" y1="19" x2="26.5" y2="19"/>
          <line x1="11" y1="14.5" x2="25" y2="14.5"/>
          <line x1="11" y1="23.5" x2="25" y2="23.5"/>
        </g>
      </svg>
      <p class="contact__text">www.techvaultgrid.com</p>
    </div>

    <div class="brand">
      <span class="brand__dot"></span>
      <p class="brand__name">TechVault Grid</p>
    </div>
  </section>
</div>
</body>
</html>
```